New Business Card Design Project VORALDI-Italy

we are VORALDI-Italy
our company in the market for 3 years we are luxury cosmetic company and its about time for a facelift :)
i will like to have elegant luxurious and unique business card
that will give the person that get it a unique, luxurious and elegant impression
I'm VERY OPEN FOR NEW IDEAS , even duo i add a few files of things that i see on line and i like them

i add my logo as well
my website is VORALDI.COM
(if you would like to see the main style that we have)

Target Market(s)

adult that have money :)

Industry/Entity Type

Business

Contact Information for Business Card

Name - Paul Voraldi
Position - CEO and CO Founder
address - 4718 E Danbury
telephone - 555-318-4402
email - paul@voraldi-example.com
fax - 555-318-4402
website - VORALDI.COM

Colors
000000
959595
fbee3e
ffffff

Requirements
Must have
• big logo in GOLD color
• elegant look
• impressive
Nice to have
• not must but maybe classy pattern background
• not must but maybe emblem
• maybe clear plastic business card
Should not have
• colors
• images

```html
<!DOCTYPE html>
<html lang="en">
<head>
<meta charset="utf-8">
<title>VORALDI Italy – Business Card</title>
<link rel="stylesheet" href="https://fonts.googleapis.com/css2?family=Open+Sans:wght@400;600;700&display=swap">
<style>
  :root {
    --backdrop: #1d1b1a;
    --card-black: #0b0b0b;
    --band-grey: #3a3a3a;
    --gold: #d8b54c;
    --white: #ffffff;
    --soft-grey: #959595;
  }
  * { margin: 0; padding: 0; box-sizing: border-box; }
  html, body {
    width: 1200px; height: 716px; overflow: hidden;
    background: var(--backdrop);
    font-family: "Open Sans", Arial, sans-serif;
  }
  .stage {
    position: relative; width: 1200px; height: 716px;
    display: flex; align-items: center; justify-content: center; gap: 40px;
  }
  .card {
    position: relative; width: 540px; height: 310px;
    background: var(--card-black);
    box-shadow: 0 14px 30px rgba(0,0,0,.55);
    overflow: hidden;
  }
  /* brand block */
  .brand {
    position: absolute; display: flex; flex-direction: column; align-items: center;
  }
  .brand-mark {
    width: 62px; height: 62px; border-radius: 50%;
    border: 3px solid var(--gold); margin-bottom: 10px;
  }
  .brand-name {
    color: var(--gold); font-weight: 600; font-size: 40px;
    letter-spacing: 4px; line-height: 1;
  }
  .brand-rule { width: 230px; height: 2px; background: var(--gold); margin: 8px 0 6px; }
  .brand-country { color: var(--gold); font-weight: 600; font-size: 13px; letter-spacing: 5px; }
  .card-front .brand { left: 0; right: 0; top: 74px; }
  .card-back .brand { left: 250px; width: 260px; top: 30px; }
  .card-back .brand-name { font-size: 34px; }
  .card-back .brand-rule { width: 200px; }
  .card-back .brand-mark { width: 54px; height: 54px; }

  .band { position: absolute; inset: 0; }
  .holder { position: absolute; left: 24px; top: 150px; }
  .holder-name { color: var(--white); font-weight: 700; font-size: 15px; }
  .holder-role { color: var(--soft-grey); font-size: 8px; }
  .contact {
    position: absolute; display: flex; flex-direction: column; gap: 5px;
    color: var(--white); font-size: 13px; font-weight: 600;
  }
  .contact-left { left: 24px; top: 212px; }
  .contact-right { left: 370px; top: 214px; }
  .contact-row { display: flex; align-items: center; gap: 8px; }
  .contact-row svg { width: 12px; height: 12px; fill: var(--gold); flex: none; }
  .address {
    position: absolute; left: 352px; top: 276px;
    display: flex; align-items: center; gap: 8px;
    color: #111; font-size: 14px; font-weight: 700;
  }
  .address svg { width: 11px; height: 13px; fill: #111; }
</style>
</head>
<body>
<main class="stage">

  <section class="card card-front">
    <div class="brand">
      <div class="brand-mark"></div>
      <div class="brand-name">VORALDI</div>
      <div class="brand-rule"></div>
      <div class="brand-country">ITALY</div>
    </div>
  </section>

  <section class="card card-back">
    <svg class="band" viewBox="0 0 540 310" aria-hidden="true">
      <polygon points="0,192 262,192 280,204 540,204 540,310 0,310" fill="#3a3a3a"/>
      <polyline points="0,192 262,192 280,204 540,204" fill="none" stroke="#d8b54c" stroke-width="2.5"/>
      <polygon points="340,270 352,262 540,262 540,296 340,296" fill="#d8b54c"/>
      <line x1="0" y1="303" x2="540" y2="303" stroke="#d8b54c" stroke-width="2"/>
    </svg>

    <div class="brand">
      <div class="brand-mark"></div>
      <div class="brand-name">VORALDI</div>
      <div class="brand-rule"></div>
      <div class="brand-country">ITALY</div>
    </div>

    <div class="holder">
      <div class="holder-name">Paul Voraldi</div>
      <div class="holder-role">Position - CEO and CO Founder</div>
    </div>

    <div class="contact contact-left">
      <div class="contact-row">
        <svg viewBox="0 0 24 24"><path d="M6.6 10.8a15 15 0 0 0 6.6 6.6l2.2-2.2a1 1 0 0 1 1-.25 11.4 11.4 0 0 0 3.6.57 1 1 0 0 1 1 1V20a1 1 0 0 1-1 1A17 17 0 0 1 3 4a1 1 0 0 1 1-1h3.5a1 1 0 0 1 1 1c0 1.25.2 2.45.57 3.57a1 1 0 0 1-.25 1z"/></svg>
        <span>555-318-4402</span>
      </div>
      <div class="contact-row">
        <svg viewBox="0 0 24 24"><path d="M2 5h20v14H2zm2 2v.5l8 5 8-5V7zm0 2.8V17h16V9.8l-8 5z"/></svg>
        <span>paul@voraldi-example.com</span>
      </div>
    </div>

    <div class="contact contact-right">
      <div class="contact-row">
        <svg viewBox="0 0 24 24"><path d="M6 2h12v6H6zM3 9h18v9h-3v4H6v-4H3zm5 7v4h8v-4z"/></svg>
        <span>555-318-4402</span>
      </div>
      <div class="contact-row">
        <svg viewBox="0 0 24 24"><path d="M12 2a10 10 0 1 0 0 20 10 10 0 0 0 0-20zm6.9 9h-3a15 15 0 0 0-1.3-6A8 8 0 0 1 18.9 11zM12 4.1c.9 1.2 1.8 3.5 2 6.9h-4c.2-3.4 1.1-5.7 2-6.9zM9.4 5A15 15 0 0 0 8.1 11h-3A8 8 0 0 1 9.4 5zM5.1 13h3a15 15 0 0 0 1.3 6A8 8 0 0 1 5.1 13zm6.9 6.9c-.9-1.2-1.8-3.5-2-6.9h4c-.2 3.4-1.1 5.7-2 6.9zm2.6-.9a15 15 0 0 0 1.3-6h3a8 8 0 0 1-4.3 6z"/></svg>
        <span>Voraldi.com</span>
      </div>
    </div>

    <div class="address">
      <svg viewBox="0 0 20 24"><path d="M10 0a8 8 0 0 0-8 8c0 6 8 16 8 16s8-10 8-16a8 8 0 0 0-8-8zm0 11a3 3 0 1 1 0-6 3 3 0 0 1 0 6z"/></svg>
      <span>4718 E Danbury</span>
    </div>
  </section>

</main>
</body>
</html>
```